Website redesign for Tawny Reef Advisory

www.tawnyreefadvisory.example

We need to redesign our not-yet-designed website. It has the basic features and most of the functionality we want, but something isn't coming together with the design and we thought we'd stop trying to get the template to do what we want it to do and let a professional design it. :)

Our key focus is digital marketing: SEO, PPC, Social Media and Local Directories. We also do web development and marketing strategy.

Websites I like:
www.coldharborstudio.example
www.lowtidewire.example
www.hikeowlonline.example

Target Market(s)

Small businesses

Industry/Entity Type

Marketing

Contact Information for Business Card

Logo, Name, Phone, email, Web, Twitter, Logo and tag on the back

Coding

Coded - Design and coding required

Number of Pages Required

2 page

Font styles to use
Serif
Sans Serif

Requirements
Must have
• Besides the information that is currently on the website, it will have two conversion areas. One conversion is for the Ratekit.io reputation management widget and the other is for an SEO site audit widget from Dunefold.example
• Only one widget is on the current website, the other needs to be added.
Nice to have
• I'd like the website to flow better than it does and have more cohesiveness. We can keep the video in the banner but it's way too big as it is, so if we do keep it we'd have to size it down considerably.
Should not have
• Can't think of anything for here but if I do, i'll add it later.

```html
<!DOCTYPE html>
<html lang="en">
<head>
<meta charset="utf-8">
<title>Tawny Reef Advisory — Digital Marketing</title>
<link href="https://fonts.googleapis.com/css2?family=Raleway:wght@400;600;700;800&family=Open+Sans:wght@400;600;700&display=swap" rel="stylesheet">
<style>
:root{
  --red:#a3212b;
  --red-dark:#8c1a23;
  --ink:#1e1e1e;
  --text:#444;
  --muted:#777;
  --grey:#f1f1f1;
  --grey-2:#e6e6e6;
  --black:#0d0d0d;
  --white:#fff;
  --orange:#e08a2c;
}
*{box-sizing:border-box;margin:0;padding:0}
html,body{width:1200px;height:3529px;overflow:hidden}
body{font-family:"Open Sans",Arial,sans-serif;color:var(--text);background:var(--white);position:relative;font-size:11px;line-height:1.6}
.abs{position:absolute}
.section-head{left:0;width:1200px}
.section-title{font-family:"Raleway",Arial,sans-serif;font-weight:800;font-size:22px;color:var(--ink);text-transform:uppercase;text-align:center;letter-spacing:.5px;line-height:1.1}
.section-sub{font-family:"Raleway",Arial,sans-serif;font-size:11px;color:#555;text-transform:uppercase;text-align:center;letter-spacing:1px;margin-top:4px}

/* header */
.site-header{left:0;top:0;width:1200px;height:90px;background:var(--white)}
.brand{left:198px;top:14px;display:flex;align-items:center;gap:10px}
.brand-mark{width:54px;height:54px;border-radius:50%;background:var(--red)}
.brand-name{font-family:"Raleway",Arial,sans-serif;font-weight:700;font-size:19px;color:var(--red);line-height:1.05;text-transform:uppercase;letter-spacing:.5px}
.top-contact{right:198px;top:14px;display:flex;gap:26px;font-size:10px;color:var(--muted)}
.top-contact span{display:flex;align-items:center;gap:5px}
.main-nav{right:198px;top:50px;display:flex;align-items:center;gap:38px;font-family:"Raleway",Arial,sans-serif;font-size:10px;font-weight:600;color:#333;text-transform:uppercase;letter-spacing:1px}
.main-nav .active{color:var(--red)}
.btn-pill{background:var(--red);color:var(--white);border-radius:16px;padding:8px 20px}

/* hero */
.hero{left:0;top:90px;width:1200px;height:529px;background:linear-gradient(135deg,#d9d9d9 0%,#f4f4f4 35%,#e3e3e3 60%,#cfcfcf 100%)}
.hero-title{left:0;width:1200px;top:298px;text-align:center;font-family:"Raleway",Arial,sans-serif;font-weight:800;font-size:52px;line-height:1.1;color:#1a1a1a;letter-spacing:1px}
.hero-sub{left:0;width:1200px;top:364px;text-align:center;font-family:"Raleway",Arial,sans-serif;font-weight:700;font-size:12px;line-height:1.4;letter-spacing:1.5px;color:#222}
.dots{display:flex;gap:6px}
.dots i{width:8px;height:8px;border-radius:50%;background:#bbb;display:block}
.dots i.on{background:var(--red)}

/* results */
.results-intro{left:198px;top:686px;width:432px}
.results-intro h3{font-family:"Raleway",Arial,sans-serif;font-weight:800;font-size:20px;color:var(--ink);line-height:1.3}
.results-intro .kicker{font-family:"Raleway",Arial,sans-serif;font-size:11px;font-weight:600;text-transform:uppercase;color:#555;letter-spacing:.5px;margin-bottom:14px}
.results-intro p{margin-bottom:12px;font-size:10.5px}
.feature-list{left:678px;top:686px;width:330px}
.feature{display:flex;gap:18px;margin-bottom:22px}
.feature .icon{flex:0 0 47px;height:47px;background:var(--ink);display:flex;align-items:center;justify-content:center}
.feature .icon.red{background:var(--red)}
.feature h4{font-family:"Raleway",Arial,sans-serif;font-weight:600;font-size:14px;color:var(--ink);margin-bottom:3px}
.feature p{font-size:10px;line-height:1.55}

/* clients */
.clients{left:0;top:1054px;width:1200px;height:306px;background:var(--grey)}
.clients-panel{left:660px;top:1150px;width:540px;height:190px;background:var(--white)}
.clients-head{left:198px;top:1120px}
.clients-head h3{font-family:"Raleway",Arial,sans-serif;font-weight:800;font-size:20px;color:var(--ink);line-height:1.3}
.clients-head div{font-family:"Raleway",Arial,sans-serif;font-size:11px;font-weight:600;color:#555;text-transform:uppercase}
.quote-mark{left:198px;top:1196px;font-family:Georgia,serif;font-size:70px;line-height:1;color:var(--ink);font-weight:700}
.quote-text{left:265px;top:1196px;width:370px;font-size:10px}
.quote-by{left:265px;top:1278px;font-size:10px;text-transform:uppercase;color:#333}
.quote-by span{display:block;color:var(--orange)}
.portrait{width:92px;height:92px;border-radius:50%;border:3px solid var(--white);box-shadow:0 2px 6px rgba(0,0,0,.2)}

/* services */
.services-intro{left:198px;top:1484px;width:804px;text-align:center;font-size:11.5px;color:#555}
.service{width:250px;display:flex;gap:16px}
.service .icon{flex:0 0 47px;height:47px;background:var(--ink);display:flex;align-items:center;justify-content:center}
.service .icon.red{background:var(--red)}
.service h4{font-family:"Raleway",Arial,sans-serif;font-weight:600;font-size:14px;color:var(--ink);margin-bottom:4px}
.service p{font-size:9.5px;line-height:1.55}

/* plans */
.plans{left:0;top:1807px;width:1200px;height:466px;background:var(--grey)}
.plan{width:182px;height:295px;top:1929px;background:var(--white);text-align:center;box-shadow:0 1px 4px rgba(0,0,0,.06)}
.plan.featured{box-shadow:0 6px 18px rgba(0,0,0,.14)}
.plan h4{font-family:"Raleway",Arial,sans-serif;font-weight:700;font-size:10.5px;color:var(--ink);text-transform:uppercase;height:56px;display:flex;align-items:center;justify-content:center;padding:0 14px;border-bottom:1px solid #eee;line-height:1.35}
.plan .price{font-size:12px;color:#333;padding:10px 0;border-bottom:1px solid #eee}
.plan .price b{color:var(--orange);font-weight:400}
.plan ul{list-style:none;font-size:10px;line-height:1.9;padding:18px 12px 0;height:152px}
.plan .btn{display:inline-block;background:var(--ink);color:var(--white);font-size:9px;font-weight:600;text-transform:uppercase;padding:6px 24px;border-radius:14px;letter-spacing:.5px}
.plan .btn.red{background:var(--red)}

/* conversion band: reputation + SEO audit */
.reputation{left:0;top:2315px;width:1200px;height:297px;background:radial-gradient(ellipse at 50% 40%,#2a2a2a 0%,#0a0a0a 70%)}
.reputation-copy{left:190px;top:2386px;width:820px;text-align:center;color:#ddd;font-family:"Raleway",Arial,sans-serif;font-size:14px;line-height:1.55}
.form-group-title{font-family:"Raleway",Arial,sans-serif;font-size:10px;font-weight:700;color:var(--white);text-transform:uppercase;letter-spacing:1px}
.field-label{font-size:10px;color:#eee;line-height:1.2}
.field{height:33px;background:var(--white)}
.scan-btn{background:var(--red);color:var(--white);font-size:11px;text-transform:uppercase;letter-spacing:.5px;display:flex;align-items:center;justify-content:center;height:33px}

/* blog */
.post{width:184px;top:2730px;background:var(--white);box-shadow:0 1px 5px rgba(0,0,0,.12);height:200px}
.post .thumb{height:106px;position:relative}
.post .date{position:absolute;left:32px;top:0;width:28px;height:30px;background:var(--ink)}
.post h5{font-size:10px;color:var(--ink);font-weight:700;padding:10px 12px 4px}
.post p{font-size:8.5px;padding:0 12px;line-height:1.55;color:#555}
.post p a{color:var(--red);font-weight:700;text-decoration:none}

/* call to action */
.cta{left:0;top:2977px;width:1200px;height:120px;background:var(--red-dark)}
.cta-title{left:206px;top:3000px;font-family:"Raleway",Arial,sans-serif;font-weight:800;font-size:20px;line-height:1.3;color:var(--white);letter-spacing:.5px}
.cta-text{left:206px;top:3030px;width:540px;font-size:9px;color:#f2d6d8;text-transform:uppercase;letter-spacing:.6px;line-height:1.6}
.quote-btn{left:784px;top:3019px;width:211px;height:34px;background:#1a1a1a;color:var(--white);font-size:11px;letter-spacing:.5px;display:flex;align-items:center;justify-content:center;text-transform:uppercase}

/* contact */
.contact-info{left:258px;top:3246px;font-size:11px;color:#333}
.contact-info dt{font-family:"Raleway",Arial,sans-serif;text-transform:uppercase;letter-spacing:2px;font-size:11px;color:#555}
.contact-info dd{margin-bottom:14px;line-height:1.4}
.contact-form{left:471px;top:3224px;width:470px;height:200px;background:var(--grey-2)}
.input{background:var(--white);height:30px;font-size:8px;color:#999;padding:9px 8px;text-transform:uppercase;line-height:1.2}
.send-btn{background:var(--red);color:var(--white);font-size:9px;font-weight:700;text-transform:uppercase;display:flex;align-items:center;justify-content:center}
.form-note{left:471px;top:3432px;font-size:8.5px;color:#777;text-transform:uppercase}

/* footer */
.site-footer{left:0;top:3478px;width:1200px;height:51px;background:var(--black)}
.copyright{left:198px;top:3497px;font-size:9px;color:#ccc}
.social{left:908px;top:3490px;display:flex;gap:8px}
.social i{width:22px;height:22px;border-radius:50%;display:block}
</style>
</head>
<body>

<!-- header -->
<header class="site-header abs"></header>
<div class="brand abs">
  <div class="brand-mark"></div>
  <div class="brand-name">Tawny Reef<br>Advisory</div>
</div>
<div class="top-contact abs">
  <span><svg width="8" height="12" viewBox="0 0 8 12"><rect x="0.5" y="0.5" width="7" height="11" rx="1.2" fill="none" stroke="#777"/><circle cx="4" cy="9.5" r=".8" fill="#777"/></svg>0912 4478 3305</span>
  <span><svg width="12" height="9" viewBox="0 0 12 9"><rect x=".5" y=".5" width="11" height="8" fill="none" stroke="#777"/><path d="M.5 .5 6 5l5.5-4.5" fill="none" stroke="#777"/></svg>HELLO@TAWNYREEFADVISORY.EXAMPLE</span>
</div>
<nav class="main-nav abs">
  <span class="active">Home</span><span>About</span><span>Services</span><span>Contact</span><span>Blog ⌄</span><span class="btn-pill">Contact Us</span>
</nav>

<!-- hero -->
<section class="hero abs" role="img" aria-label="Photo of business people at a desk reviewing documents with glasses and a wristwatch"></section>
<h1 class="hero-title abs">WE ARE TAWNY REEF</h1>
<div class="hero-sub abs">WE HELP YOUR BUSINESS WIN THE INTERNET</div>
<div class="dots abs" style="left:578px;top:591px"><i class="on"></i><i></i><i></i><i></i></div>

<!-- big results -->
<div class="results-intro abs">
  <h3>BIG RESULTS FOR YOUR BUSINESS</h3>
  <div class="kicker">The who, what and why our company exists</div>
  <p>Tawny Reef's digital marketing services provide big results at affordable prices, making unperfect fit for businesses of all types who need a bigger online footprint in order to grow.</p>
  <p>We create custom digital marketing strategies for businesses of all sizes, from web design and search engine optimization (SEO) to pay-per-click (PPC) campaigns and search engine reputation management (SERM). We work with you, step by step, to develop, implement, and monitor a digital marketing plan specifically tailored to the unique needs of your business.</p>
  <p>Tawny Reef is not our first time at the digital marketing rodeo. We've built our expertise providing local SEO and online reputation management services to businesses for over 10 years, and we're ready to put our experience to work for you. Our services leverage your digital marketing investment so you can run with the big dogs online – at a fraction of the cost of a big-dog advertising budget.</p>
</div>
<div class="feature-list abs">
  <div class="feature"><div class="icon red"><svg width="22" height="22" viewBox="0 0 22 22"><path d="M3 12 12 3h7v7l-9 9z" fill="none" stroke="#fff" stroke-width="2"/><circle cx="15.5" cy="6.5" r="1.5" fill="#fff"/></svg></div><div><h4>Build Your Brand</h4><p>Lorem Ipsum is simply dummy text of the printing and typesetting industry. Lorem Ipsum has been the industry's standard.</p></div></div>
  <div class="feature"><div class="icon"><svg width="22" height="22" viewBox="0 0 22 22"><circle cx="11" cy="11" r="9" fill="none" stroke="#fff" stroke-width="2"/><path d="M2 11h18M11 2c4 4 4 14 0 18M11 2c-4 4-4 14 0 18" fill="none" stroke="#fff" stroke-width="1.5"/></svg></div><div><h4>Build Your Website</h4><p>Lorem Ipsum is simply dummy text of the printing and typesetting industry. Lorem Ipsum has been the industry's standard.</p></div></div>
  <div class="feature"><div class="icon"><svg width="22" height="22" viewBox="0 0 22 22"><circle cx="11" cy="11" r="7" fill="none" stroke="#fff" stroke-width="2"/><path d="M11 1v6M11 15v6M1 11h6M15 11h6" stroke="#fff" stroke-width="2"/></svg></div><div><h4>Position Your Brand</h4><p>Lorem Ipsum is simply dummy text of the printing and typesetting industry. Lorem Ipsum has been the industry's standard.</p></div></div>
  <div class="feature"><div class="icon"><svg width="22" height="22" viewBox="0 0 22 22"><path d="M3 10h4v10H3zM8 10l4-8c2 0 2 2 2 3l-1 4h6c1 0 2 1 1.5 2.5L18 19c-.3.8-1 1-2 1H8z" fill="#fff"/></svg></div><div><h4>Build Your Reputation</h4><p>Lorem Ipsum is simply dummy text of the printing and typesetting industry. Lorem Ipsum has been the industry's standard.</p></div></div>
</div>

<!-- clients -->
<section class="clients abs"></section>
<div class="clients-panel abs"></div>
<div class="clients-head abs"><h3>CLIENTS</h3><div>Customers says about us</div></div>
<div class="quote-mark abs">“</div>
<p class="quote-text abs">Lorem Ipsum is simply dummy text of the printing and typesetting industry. Lorem Ipsum has been the industry's standard dummy text ever since the 1500s, when an unknown printer took a galley of type and scrambled it to make a type specimen book. It has survived not only five centuries...</p>
<div class="quote-by abs">By<span>Corin Vale</span></div>
<div class="portrait abs" role="img" aria-label="Client portrait photo" style="left:679px;top:1194px;background:linear-gradient(160deg,#c7633a,#2b2b2b)"></div>
<div class="portrait abs" role="img" aria-label="Client portrait photo" style="left:794px;top:1194px;background:linear-gradient(160deg,#e8a43a,#7a4a2a)"></div>
<div class="portrait abs" role="img" aria-label="Client portrait photo" style="left:907px;top:1194px;background:linear-gradient(160deg,#e7e7e7,#8a8a8a)"></div>
<div class="dots abs" style="left:822px;top:1296px"><i class="on"></i><i></i><i></i></div>

<!-- services -->
<div class="section-head abs" style="top:1424px"><h2 class="section-title">Digital Marketing Services</h2><div class="section-sub">Some of our services</div></div>
<p class="services-intro abs">Tawny Reef's digital marketing services are the cards you need for an internet-winning hand. Choose one or a combination of several services for a stronger hand, or choose them all for a hand that's unbeatable. Any of our digital marketing services will help you build your online profile – but all of them working together deliver big results.</p>
<div class="service abs" style="left:198px;top:1576px"><div class="icon red"><svg width="20" height="20" viewBox="0 0 20 20"><circle cx="8" cy="8" r="5.5" fill="none" stroke="#fff" stroke-width="2"/><path d="m12 12 6 6" stroke="#fff" stroke-width="2.5"/></svg></div><div><h4>Search Engine Optimization</h4><p>SEO determines whether your business' website will be seen by your target customers or not, and Seekwell's</p></div></div>
<div class="service abs" style="left:470px;top:1576px"><div class="icon"><svg width="20" height="20" viewBox="0 0 20 20"><circle cx="10" cy="10" r="8" fill="none" stroke="#fff" stroke-width="2"/><circle cx="10" cy="10" r="2.5" fill="#fff"/></svg></div><div><h4>Pay-Per-Click Advertising</h4><p>Boost your site to the front of the pack with Tawny Reef's pay-per-click advertising services. We zero in on</p></div></div>
<div class="service abs" style="left:744px;top:1576px"><div class="icon"><svg width="20" height="20" viewBox="0 0 20 20"><path d="M4 16 14 6l2 2L6 18H4zM13 3l4 4" stroke="#fff" stroke-width="2" fill="none"/></svg></div><div><h4>Reputation Management</h4><p>Word-of-mouth has always been the most powerful and effective marketing tool, and it's just as true online as it is in the real world.</p></div></div>
<div class="service abs" style="left:198px;top:1689px"><div class="icon"><svg width="20" height="20" viewBox="0 0 20 20"><rect x="2" y="3" width="16" height="11" fill="none" stroke="#fff" stroke-width="2"/><path d="M7 18h6M10 14v4" stroke="#fff" stroke-width="2"/></svg></div><div><h4>Website Development</h4><p>These days, if your business doesn't have a website, most potential customers will never</p></div></div>
<div class="service abs" style="left:470px;top:1689px"><div class="icon"><svg width="20" height="20" viewBox="0 0 20 20"><circle cx="10" cy="6" r="3" fill="#fff"/><circle cx="4" cy="9" r="2" fill="#fff"/><circle cx="16" cy="9" r="2" fill="#fff"/><path d="M4 18c0-4 3-7 6-7s6 3 6 7z" fill="#fff"/></svg></div><div><h4>Social Media Marketing</h4><p>Social media platforms like Chirpnest aren't just great ways to engage with existing and potential</p></div></div>
<div class="service abs" style="left:744px;top:1689px"><div class="icon"><svg width="20" height="20" viewBox="0 0 20 20"><path d="M3 17h14M5 16V10M9 16V6M13 16V8M17 16V3" stroke="#fff" stroke-width="2.2"/></svg></div><div><h4>Analytics &amp; Conversions</h4><p>Tawny Reef will help you define the best overall strategy for your business.</p></div></div>

<!-- plans -->
<section class="plans abs"></section>
<div class="section-head abs" style="top:1860px"><h2 class="section-title">Our Plans</h2><div class="section-sub">Lorem Ipsum</div></div>
<div class="plan abs" style="left:301px"><h4>Reputation Management</h4><div class="price">From <b>$100</b> per month</div><ul><li>Access to Ratekit.io Review platform</li><li>for generating reviews</li><li>Review monitoring</li></ul><span class="btn">Start Now</span></div>
<div class="plan featured abs" style="left:508px"><h4>Social Media Updates + SERM</h4><div class="price">From <b>$200</b> per month</div><ul><li>Regular Chirpnest</li><li>other social updates and</li><li>or blog posts</li><li>Includes all of our</li><li>Reputation Management services</li></ul><span class="btn red">Start Now</span></div>
<div class="plan abs" style="left:715px"><h4>Comprehensive Marketing Strategy</h4><div class="price">From <b>$250</b> per month</div><ul><li>Marketing strategy for your</li><li>business both online &amp; off</li><li>Reputation Management</li><li>Social Media Updates</li></ul><span class="btn">Start Now</span></div>

<!-- conversion band: reputation widget + SEO audit widget -->
<section class="reputation abs" role="img" aria-label="Dark faded photo of a team meeting behind the conversion forms"></section>
<div class="section-head abs" style="top:2336px"><h2 class="section-title" style="color:var(--white)">Reputation Management</h2><div class="section-sub" style="color:#ddd">Contantry popular popular sit lorem</div></div>
<p class="reputation-copy abs">Each individual plays a great role in the development of our company. All their contributions are more worth than gold making them an invaluable asset to the company.</p>

<div class="field-label abs" style="left:188px;top:2450px">Business Name</div>
<div class="field-label abs" style="left:428px;top:2450px">Postal Code</div>
<div class="field-label abs" style="left:581px;top:2450px">Business Phone</div>
<div class="field abs" style="left:188px;top:2466px;width:236px"></div>
<div class="field abs" style="left:428px;top:2466px;width:148px"></div>
<div class="field abs" style="left:581px;top:2466px;width:210px"></div>
<div class="scan-btn abs" style="left:800px;top:2466px;width:212px">Scan My Review Free</div>

<div class="form-group-title abs" style="left:188px;top:2518px">SEO Site Audit</div>
<div class="field-label abs" style="left:320px;top:2520px">Website URL</div>
<div class="field-label abs" style="left:581px;top:2520px">Email Address</div>
<div class="field abs" style="left:188px;top:2538px;width:388px"></div>
<div class="field abs" style="left:581px;top:2538px;width:210px"></div>
<div class="scan-btn abs" style="left:800px;top:2538px;width:212px">Run My SEO Audit</div>

<!-- blog -->
<div class="section-head abs" style="top:2660px"><h2 class="section-title">Latest Blog</h2><div class="section-sub">Lorem Ipsum</div></div>
<article class="post abs" style="left:198px"><div class="thumb" role="img" aria-label="Photo of business people silhouetted against a city window" style="background:linear-gradient(135deg,#2d4a6e,#0e1a2c)"><span class="date"></span></div><h5>Blog Post Title Here</h5><p>It is a long established fact that a reader will be distracted by the readable content of a page when looking at its layout. <a>Read More</a></p></article>
<article class="post abs" style="left:405px"><div class="thumb" role="img" aria-label="Photo of colleagues talking at a laptop" style="background:linear-gradient(135deg,#d8d8d8,#5b6470)"><span class="date"></span></div><h5>Blog Post Title Here</h5><p>It is a long established fact that a reader will be distracted by the readable content of a page when looking at its layout. <a>Read More</a></p></article>
<article class="post abs" style="left:609px"><div class="thumb" role="img" aria-label="Photo of a team meeting in a bright office" style="background:linear-gradient(135deg,#f0f0f0,#9aa0a6)"><span class="date"></span></div><h5>Blog Post Title Here</h5><p>It is a long established fact that a reader will be distracted by the readable content of a page when looking at its layout. <a>Read More</a></p></article>
<article class="post abs" style="left:816px"><div class="thumb" role="img" aria-label="Photo of a hand touching a glowing digital network screen" style="background:linear-gradient(135deg,#3c86c4,#0f2b4e)"><span class="date"></span></div><h5>Blog Post Title Here</h5><p>It is a long established fact that a reader will be distracted by the readable content of a page when looking at its layout. <a>Read More</a></p></article>

<!-- call to action -->
<section class="cta abs"></section>
<h3 class="cta-title abs">READY TO WIN THE INTERNET?</h3>
<p class="cta-text abs">Get in touch. We're happy to answer any questions you have, and ready to start developing your custom digital marketing strategy to win the internet for your business.</p>
<div class="quote-btn abs">Get a Quote</div>

<!-- contact -->
<div class="section-head abs" style="top:3152px"><h2 class="section-title">Contact Us</h2><div class="section-sub">Lorem Ipsum</div></div>
<dl class="contact-info abs">
  <dt>Call Me</dt><dd>P: 0912 4478 3305</dd>
  <dt>Email Me</dt><dd>HELLO@TAWNYREEFADVISORY.EXAMPLE</dd>
  <dt>Address</dt><dd>48 Saltmarsh Lane, 9th Floor<br>Port Alden<br>United States</dd>
</dl>
<div class="contact-form abs"></div>
<div class="input abs" style="left:494px;top:3264px;width:188px">Name</div>
<div class="input abs" style="left:494px;top:3306px;width:188px">Email</div>
<div class="input abs" style="left:494px;top:3348px;width:188px">Subject</div>
<div class="input abs" style="left:704px;top:3264px;width:216px;height:72px">Texts</div>
<div class="send-btn abs" style="left:704px;top:3350px;width:216px;height:28px">Send Now</div>
<div class="form-note abs">Looking forward to hearing from you!</div>

<!-- footer -->
<footer class="site-footer abs"></footer>
<div class="copyright abs">Copyright © 2016 yoursite All rights reserved</div>
<div class="social abs"><i style="background:#c4412f"></i><i style="background:#3f729b"></i><i style="background:#2aa3ef"></i><i style="background:#3b5998"></i></div>

</body>
</html>
```